Harrowgate Distillery Bottle Label Design

We need a label design for a product called "Cedar Lorne Straight Bourbon Whiskey". The bottle has two embossments on the side and an image printed on the back that will show through when looking from the front (shown in the attached image). It's made of 30% rye and 70% corn; images of the ingredients can be incorporated into the label design. We are a distillery that produces whiskey and bourbon from local farmers around the area. We focus on the quality of the ingredients and using the recipes passed down from generation to generation. We like a straight forward design using two colors maximum. The background will be brown once filled with the bourbon, so it must contrast against it (i.e. white and other lighter colors). The Harrowgate Distillery logo must be present on the bottle front, as well as 750 ml, 84 PROOF, 42% ALC/VOL.

Target Market(s)

Craft whiskey consumers.

Industry/Entity Type

Product

Colors
fee18a
fbe7d2
fff3d1
fefcee
fefdec
fdf9cf

Requirements
Must have
• 750 ml, 84 PROOF, 42% ALC/VOL. Aged for 3 years.The Harrowgate Distillery logo must be present on the bottle. Only two colors on label.
Nice to have
• Story of how we are a micro distillery making hand crafted whiskey.
Should not have
• False or misleading print.

```html
<!DOCTYPE html>
<html lang="en">
<head>
<meta charset="utf-8">
<title>Cedar Lorne Straight Bourbon Whiskey – Harrowgate Distillery Label</title>
<link href="https://fonts.googleapis.com/css2?family=Rye&family=Cinzel:wght@700&family=Montserrat:wght@500;700;800&display=swap" rel="stylesheet">
<style>
  :root {
    --backdrop: #e6e6e4;
    --label-light: #f4f3e2;
    --label-dark: #e3e2c9;
    --ink: #1d1b18;
    --accent-red: #c23a27;
    --still-copper: #8d8776;
    --still-light: #cfcdb9;
  }
  * { margin: 0; padding: 0; box-sizing: border-box; }
  html, body {
    width: 1200px; height: 2514px; overflow: hidden;
    background: var(--backdrop);
  }
  .label {
    position: absolute; left: 60px; top: 412px;
    width: 1080px; height: 1690px;
    background: linear-gradient(90deg, var(--label-dark) 0%, var(--label-light) 30%, var(--label-light) 70%, var(--label-dark) 100%);
    color: var(--ink);
  }
  .label > * { position: absolute; }
  .brand-mark {
    left: 130px; top: 58px; width: 130px; height: 130px;
    border-radius: 50%; background: var(--ink);
  }
  .brand-name {
    left: 300px; top: 62px;
    font-family: "Montserrat", sans-serif; font-weight: 800;
    font-size: 86px; line-height: 1; letter-spacing: -1px;
  }
  .brand-rule {
    left: 300px; top: 160px; width: 470px; height: 3px; background: var(--ink);
  }
  .brand-sub {
    left: 300px; top: 168px;
    font-family: "Montserrat", sans-serif; font-weight: 700;
    font-size: 32px; line-height: 1; letter-spacing: 9px;
  }
  .still-illustration {
    left: 130px; top: 220px; width: 720px; height: 640px;
    background: radial-gradient(ellipse at 50% 55%, var(--still-copper) 0%, var(--still-light) 55%, transparent 75%);
    border-radius: 12px;
  }
  .product-name {
    left: 0; top: 880px; width: 100%; text-align: center;
    font-family: "Rye", serif; font-size: 112px; line-height: 1.5;
    white-space: nowrap; text-transform: uppercase;
  }
  .product-name .initial { font-size: 150px; }
  .name-rule {
    left: 490px; top: 1118px; width: 100px; height: 3px; background: var(--ink);
  }
  .product-type {
    left: 0; top: 1145px; width: 100%; text-align: center;
    font-family: "Cinzel", serif; font-weight: 700;
    font-size: 46px; letter-spacing: 2px; text-transform: uppercase;
  }
  .age-block {
    left: 0; top: 1262px; width: 100%; text-align: center;
    font-family: "Montserrat", sans-serif; font-weight: 700;
  }
  .age-caption { font-size: 20px; letter-spacing: 3px; line-height: 1; }
  .age-number {
    display: flex; justify-content: center; align-items: center; gap: 18px;
    color: var(--accent-red); font-size: 96px; font-weight: 800; line-height: 1.05;
  }
  .age-lines { width: 70px; height: 40px; }
  .rule { height: 3px; background: var(--ink); }
  .rule-top { left: 220px; top: 1430px; width: 760px; }
  .rule-mid { left: 100px; top: 1540px; width: 880px; }
  .rule-bottom { left: 100px; top: 1632px; width: 880px; }
  .vrule { width: 3px; background: var(--ink); }
  .proof-left { left: 318px; top: 1430px; height: 110px; }
  .proof-right { left: 757px; top: 1430px; height: 110px; }
  .proof {
    left: 318px; width: 442px; top: 1455px; text-align: center;
    font-family: "Montserrat", sans-serif; font-weight: 700; font-size: 54px; line-height: 1.1;
  }
  .volume-divider { left: 425px; top: 1552px; height: 70px; }
  .volume, .abv {
    top: 1562px; font-family: "Montserrat", sans-serif; font-weight: 500;
    font-size: 40px; line-height: 1.2;
  }
  .volume { left: 130px; width: 270px; text-align: center; }
  .abv { left: 450px; width: 530px; text-align: center; }
</style>
</head>
<body>
  <main class="label">
    <div class="brand-mark"></div>
    <div class="brand-name">Harrowgate</div>
    <div class="brand-rule"></div>
    <div class="brand-sub">DISTILLERY</div>

    <div class="still-illustration" role="img" aria-label="Engraved illustration of a copper pot still connected by a swan-neck pipe to a condenser"></div>

    <h1 class="product-name"><span class="initial">C</span>edar <span class="initial">L</span>orne</h1>
    <div class="name-rule"></div>
    <h2 class="product-type">Straight Bourbon Whiskey</h2>

    <div class="age-block">
      <div class="age-caption">AGED FOR</div>
      <div class="age-number">
        <svg class="age-lines" viewBox="0 0 70 40"><g stroke="#1d1b18" stroke-width="3"><line x1="0" y1="8" x2="70" y2="8"/><line x1="20" y1="20" x2="70" y2="20"/><line x1="0" y1="32" x2="70" y2="32"/></g></svg>
        <span>3</span>
        <svg class="age-lines" viewBox="0 0 70 40"><g stroke="#1d1b18" stroke-width="3"><line x1="0" y1="8" x2="70" y2="8"/><line x1="0" y1="20" x2="50" y2="20"/><line x1="0" y1="32" x2="70" y2="32"/></g></svg>
      </div>
      <div class="age-caption">YEARS</div>
    </div>

    <div class="rule rule-top"></div>
    <div class="vrule proof-left"></div>
    <div class="vrule proof-right"></div>
    <div class="proof">84 PROOF</div>
    <div class="rule rule-mid"></div>
    <div class="volume">750 ML</div>
    <div class="vrule volume-divider"></div>
    <div class="abv">42% ALC/VOL.</div>
    <div class="rule rule-bottom"></div>
  </main>
</body>
</html>
```